Feng Shui Consultant needing a business card designed

please incorporate the following colours in the design: lilac (primarily)black and gold
Name of the business is: Heron Feng Shui
The main design should incorporate a willow tree, to be the main focus of the design
The design should be modern and sophisticated
The back of the card should include the following details;
name; Maribel Costade
title: Accredited Feng Shui Consultant
phone number; 0472 915 384
email address; maribel_costade@quillpost.example
Specialising in Feng Shui and Space Clearing

Highend, affluent white collar clients. Well educated

Business

e3daeb

```html
<!DOCTYPE html>
<html lang="en">
<head>
<meta charset="utf-8">
<title>Heron Feng Shui — Business Card</title>
<link rel="stylesheet" href="https://fonts.googleapis.com/css2?family=Jost:wght@400;500&display=swap">
<style>
  :root {
    --backdrop: #ececee;
    --lilac: #e3daeb;
    --lilac-pattern: #cdc1e4;
    --lilac-deep: #b9a9da;
    --ink: #1d1a1e;
    --gold: #a18a2c;
  }
  * { box-sizing: border-box; margin: 0; padding: 0; }
  html, body { width: 1200px; height: 900px; overflow: hidden; }
  body {
    background: var(--backdrop);
    font-family: "Jost", "Futura", sans-serif;
    color: var(--ink);
    position: relative;
  }
  .card {
    position: absolute;
    top: 135px;
    width: 390px;
    height: 630px;
    background: var(--lilac);
    box-shadow: 0 4px 14px rgba(0,0,0,0.18);
    overflow: hidden;
  }
  .card--front { left: 190px; }
  .card--back { left: 620px; }

  .pattern-band {
    position: absolute;
    left: 0;
    width: 100%;
    z-index: 0;
    background: linear-gradient(to bottom, var(--lilac-pattern), var(--lilac));
  }
  .pattern-band--top { top: 0; }
  .pattern-band--bottom { bottom: 0; background: linear-gradient(to top, var(--lilac-pattern), var(--lilac)); }
  .card--front .pattern-band--top { height: 75px; }
  .card--front .pattern-band--bottom { height: 100px; }
  .card--back .pattern-band--top { height: 100px; }
  .card--back .pattern-band--bottom { height: 75px; }

  .brand {
    position: absolute;
    left: 0;
    width: 100%;
    z-index: 1;
    text-align: center;
    font-weight: 400;
    color: var(--ink);
    text-transform: uppercase;
  }
  .brand__mark {
    display: block;
    margin: 0 auto;
    border-radius: 50%;
    background: var(--lilac-deep);
  }
  .brand__wordmark {
    margin: 0 auto;
    border-top: 1.5px solid var(--gold);
    border-bottom: 1.5px solid var(--gold);
  }
  .card--front .brand { top: 125px; }
  .card--front .brand__mark { width: 200px; height: 200px; margin-bottom: 45px; }
  .card--front .brand__wordmark { width: 200px; padding: 10px 0 8px; }
  .card--front .brand__name { font-size: 44px; letter-spacing: 4px; line-height: 1.05; }
  .card--front .brand__sub { font-size: 19px; letter-spacing: 5px; }

  .card--back .brand { top: 125px; }
  .card--back .brand__mark { width: 100px; height: 100px; margin-bottom: 14px; }
  .card--back .brand__wordmark { width: 98px; padding: 5px 0 4px; }
  .card--back .brand__name { font-size: 22px; letter-spacing: 2px; line-height: 1.05; }
  .card--back .brand__sub { font-size: 10px; letter-spacing: 3px; }

  .contact {
    position: absolute;
    top: 352px;
    left: 0;
    width: 100%;
    z-index: 1;
    text-align: center;
  }
  .contact__name {
    font-size: 23px;
    letter-spacing: 6px;
    text-transform: uppercase;
    font-weight: 400;
  }
  .contact__title {
    margin-top: 2px;
    font-size: 14px;
    color: var(--gold);
    text-transform: uppercase;
  }
  .contact__lines {
    margin-top: 22px;
    font-size: 15px;
    line-height: 1.75;
    list-style: none;
  }
  .contact__label { color: var(--gold); margin-right: 4px; }
  .contact__specialty {
    margin-top: 14px;
    font-size: 14px;
    text-transform: uppercase;
    line-height: 1.45;
  }
</style>
</head>
<body>
  <section class="card card--front">
    <div class="pattern-band pattern-band--top" role="img" aria-label="Lilac seigaiha wave pattern border"></div>
    <div class="brand">
      <span class="brand__mark"></span>
      <div class="brand__wordmark">
        <div class="brand__name">Heron</div>
        <div class="brand__sub">Feng Shui</div>
      </div>
    </div>
    <div class="pattern-band pattern-band--bottom" role="img" aria-label="Lilac seigaiha wave pattern border"></div>
  </section>

  <section class="card card--back">
    <div class="pattern-band pattern-band--top" role="img" aria-label="Lilac seigaiha wave pattern border"></div>
    <div class="brand">
      <span class="brand__mark"></span>
      <div class="brand__wordmark">
        <div class="brand__name">Heron</div>
        <div class="brand__sub">Feng Shui</div>
      </div>
    </div>
    <div class="contact">
      <h1 class="contact__name">Maribel Costade</h1>
      <p class="contact__title">Accredited Feng Shui Consultant</p>
      <ul class="contact__lines">
        <li><span class="contact__label">P:</span>0472 915 384</li>
        <li><span class="contact__label">E:</span>maribel_costade@quillpost.example</li>
      </ul>
      <p class="contact__specialty">Specialising in Feng Shui<br>and Space Clearing.</p>
    </div>
    <div class="pattern-band pattern-band--bottom" role="img" aria-label="Lilac seigaiha wave pattern border"></div>
  </section>
</body>
</html>
```